Meridel Haulage - Website

A clean, not cluttered informative website for our business. We specialize in the transportation of radioactive materials across North America. The site is mostly for information about our company and will not be used to attract business but will be used to attract employee's mainly drivers. Driver's are very hard to find in our area. One of the pages needs to be a job's posting page with an apply now button. Either an application can be filled out there or a resume can be uploaded which ever functionality works better. I would like a website that I can easily edit, ability to change text and photos.

Number of Pages Required

5+ page

Colors

Designer to choose colors to be used in the design.

Requirements
Must have
• Home - About - Services - Jobs - Contact pages
• A way prospective employee's can apply or upload their resume to be emailed to me
• Very clean apperance
Should not have
• I don't want it to be busy

```html
<!DOCTYPE html>
<html lang="en">
<head>
<meta charset="utf-8">
<title>Meridel Haulage</title>
<link href="https://fonts.googleapis.com/css2?family=Open+Sans:wght@400;600;700&family=Roboto:wght@500;700;900&display=swap" rel="stylesheet">
<style>
:root{
  --blue:#1b5eab;
  --blue-dark:#134a8a;
  --ink:#1d1d1d;
  --text:#555;
  --grey-band:#e6e6e6;
  --row-alt:#edf0f4;
  --line:#cfcfcf;
  --footer:#141414;
  --white:#fff;
}
*{box-sizing:border-box;margin:0;padding:0}
html,body{width:1200px;height:3711px;overflow:hidden;background:var(--white)}
body{position:relative;font-family:'Open Sans',sans-serif;color:var(--text)}
.abs{position:absolute}
.heading{font-family:'Roboto',sans-serif;font-weight:700;color:var(--ink);text-transform:uppercase}
.btn-outline{display:flex;align-items:center;justify-content:center;border:2px solid var(--blue);border-radius:30px;color:var(--blue);font-family:'Roboto',sans-serif;font-weight:700;font-size:17px;letter-spacing:.5px;background:var(--white)}
.btn-solid{display:flex;align-items:center;justify-content:center;border-radius:30px;background:var(--blue);color:var(--white);font-family:'Roboto',sans-serif;font-weight:700;font-size:15px;letter-spacing:.4px}

/* header */
.site-header{left:0;top:0;width:1200px;height:100px;background:var(--white)}
.brand{left:112px;top:22px;font-family:'Roboto',sans-serif;font-weight:900;font-size:34px;color:var(--blue);line-height:1;letter-spacing:1px;text-transform:uppercase;display:flex;align-items:center;gap:12px}
.brand-dot{width:18px;height:18px;background:var(--blue);border-radius:50%}
.nav{right:108px;top:40px;display:flex;gap:38px;font-family:'Roboto',sans-serif;font-weight:700;font-size:16px;color:var(--ink)}
.nav .active{color:var(--blue)}

/* hero */
.hero{left:0;top:100px;width:1200px;height:606px}
.hero-title{left:0;top:210px;width:1200px;text-align:center;font-family:'Roboto',sans-serif;font-weight:700;font-size:66px;color:var(--white);text-transform:uppercase}
.hero-sub{left:300px;top:308px;width:600px;text-align:center;font-size:27px;line-height:41px;color:var(--white);font-weight:600}
.hero-btn{left:494px;top:441px;width:212px;height:60px;border:2px solid var(--white);border-radius:30px;color:var(--white);font-family:'Roboto',sans-serif;font-weight:700;font-size:17px;display:flex;align-items:center;justify-content:center}
.dots{left:565px;top:588px;display:flex;gap:5px}
.dots span{width:13px;height:13px;border-radius:50%;border:2px solid var(--white)}
.dots span.on{background:var(--white)}

/* welcome */
.welcome-title{left:0;top:822px;width:1200px;text-align:center;font-size:40px}
.welcome-text{left:270px;top:898px;width:660px;text-align:center;font-size:15.5px;line-height:27px}
.welcome-text p+p{margin-top:26px}
.video{left:396px;top:1083px;width:408px;height:255px}
.about-btn{left:527px;top:1393px;width:146px;height:54px}

/* services */
.services-bg{left:0;top:1540px}
.services-title{left:200px;top:1612px;width:332px;text-align:center;font-size:38px}
.services-text{left:111px;top:1764px;width:570px;font-size:15.5px;line-height:26px;color:var(--white)}
.services-text p+p{margin-top:24px}
.read-btn{left:111px;top:2009px;width:148px;height:54px;border:2px solid var(--white);border-radius:30px;color:var(--white);font-family:'Roboto',sans-serif;font-weight:700;font-size:17px;display:flex;align-items:center;justify-content:center}
.services-photo{left:750px;top:1648px}

/* jobs */
.jobs-title{left:0;top:2264px;width:1200px;text-align:center;font-size:40px}
.jobs-intro{left:230px;top:2340px;width:740px;text-align:center;font-size:15.5px;line-height:27px}
.jobs-table{left:237px;top:2474px;width:725px;border-collapse:collapse}
.jobs-table td{border:1.5px solid var(--line);height:133px;vertical-align:middle}
.jobs-table tr:nth-child(2) td{background:var(--row-alt)}
.job-photo{width:151px;padding:0 0 0 16px}
.job-photo div{width:117px;height:100px;background:linear-gradient(135deg,#6b6f68,#2f3a34)}
.job-text{width:416px;padding:0 24px 0 24px;font-size:14.5px;line-height:24px}
.job-apply{width:158px}
.job-apply .btn-solid{width:128px;height:44px;margin:0 auto}
.view-btn{left:527px;top:2929px;width:146px;height:55px}

/* footer */
.footer-bg{left:0;top:3090px}
.footer-heading{font-family:'Roboto',sans-serif;font-weight:700;font-size:20px;color:var(--white);text-transform:uppercase}
.form-title{left:111px;top:3268px}
.field{background:var(--white);font-size:12px;color:#666;padding:6px 10px;height:32px}
.f1{left:111px;top:3338px;width:312px}
.f2{left:431px;top:3338px;width:311px}
.f3{left:111px;top:3385px;width:312px}
.f4{left:431px;top:3385px;width:311px}
.f5{left:111px;top:3431px;width:631px;height:84px}
.submit{left:633px;top:3533px;width:112px;height:45px}
.info-title{left:804px;top:3268px}
.info-row{left:804px;display:flex;align-items:center;gap:17px;color:var(--white);font-size:14.5px;line-height:23px}
.icon{width:34px;height:34px;border:1.5px solid var(--white);border-radius:50%;display:flex;align-items:center;justify-content:center;flex:none}
.socials{left:806px;top:3538px;display:flex;gap:10px}
.socials span{width:32px;height:32px;border-radius:50%}
.divider{left:99px;top:3620px;width:1002px;height:1px;background:#3a3a3a}
.copyright{left:0;top:3646px;width:1200px;text-align:center;color:var(--white);font-size:14px}
</style>
</head>
<body>

<header class="abs site-header">
  <div class="abs brand"><span class="brand-dot"></span>Meridel Haulage</div>
  <nav class="abs nav">
    <span class="active">HOME</span><span>ABOUT</span><span>SERVICES</span><span>JOBS</span><span>CONTACT</span>
    <svg width="16" height="16" viewBox="0 0 16 16"><circle cx="6.5" cy="6.5" r="5" fill="none" stroke="#1d1d1d" stroke-width="2.2"/><line x1="10.3" y1="10.3" x2="15" y2="15" stroke="#1d1d1d" stroke-width="2.6" stroke-linecap="round"/></svg>
  </nav>
</header>

<svg class="abs hero" width="1200" height="606" viewBox="0 0 1200 606" role="img" aria-label="Photo of a tractor-trailer carrying sealed barrels for radioactive material transport">
  <defs>
    <linearGradient id="heroGrad" x1="0" y1="0" x2="0" y2="1">
      <stop offset="0" stop-color="#6f7274"/>
      <stop offset=".55" stop-color="#4d5153"/>
      <stop offset="1" stop-color="#2e3133"/>
    </linearGradient>
  </defs>
  <polygon points="0,0 1200,0 1200,513 371,606 0,513" fill="url(#heroGrad)"/>
</svg>
<div class="abs hero-title">Meridel Haulage</div>
<div class="abs hero-sub">We specialize in the transportation of radioactive materials across North America.</div>
<div class="abs hero-btn">GET MORE INFO</div>
<div class="abs dots"><span class="on"></span><span></span><span></span><span></span></div>

<h2 class="abs heading welcome-title">Welcome to Meridel Haulage</h2>
<div class="abs welcome-text">
  <p>With a firm commitment to superior service and integrity above all, the Meridel Haulage team has developed an enviable reputation within the transportation industry.</p>
  <p>Our mission is to make our customers both satisfied and successful, and our continuing growth testifies to the sincerity of our dedication.</p>
</div>
<svg class="abs video" width="408" height="255" viewBox="0 0 408 255" role="img" aria-label="Video still of a tanker truck beside storage silos">
  <defs>
    <linearGradient id="vidGrad" x1="0" y1="0" x2="0" y2="1">
      <stop offset="0" stop-color="#8fb3d8"/>
      <stop offset=".45" stop-color="#c9cdd1"/>
      <stop offset="1" stop-color="#6d7278"/>
    </linearGradient>
  </defs>
  <rect width="408" height="255" fill="url(#vidGrad)"/>
  <circle cx="204" cy="127" r="30" fill="rgba(0,0,0,.25)" stroke="#fff" stroke-width="3"/>
  <polygon points="196,113 196,141 219,127" fill="#fff"/>
</svg>
<div class="abs btn-outline about-btn">ABOUT US</div>

<svg class="abs services-bg" width="1200" height="630" viewBox="0 1540 1200 630">
  <polygon points="0,1640 383,1551 742,1650 0,1781" fill="var(--grey-band)"/>
  <polygon points="0,1781 1200,1568 1200,2098 383,2165 0,2098" fill="var(--blue)"/>
</svg>
<h2 class="abs heading services-title">Our Services</h2>
<div class="abs services-text">
  <p>At Meridel Haulage, we specialize in both expedited and regular LTL, Partial Load and Full Truck Load service between Canada, the USA, and Mexico.</p>
  <p>In addition, to meet our just in time door to door service requirements, our policy includes one line hauls right to your delivery, which eliminates extra handling of your products which also in turn reduces damages and claims. Our operations staff monitor transit times for every shipment with our satellite tracking and communications network installed in every power unit.</p>
</div>
<div class="abs read-btn">READ MORE</div>
<svg class="abs services-photo" width="340" height="404" viewBox="0 0 340 404" role="img" aria-label="Photo of blue sealed chemical drums viewed from above">
  <defs>
    <linearGradient id="drumGrad" x1="0" y1="0" x2="1" y2="1">
      <stop offset="0" stop-color="#6fa9e8"/>
      <stop offset=".5" stop-color="#2a6cc4"/>
      <stop offset="1" stop-color="#123f82"/>
    </linearGradient>
  </defs>
  <polygon points="8,28 334,4 330,378 4,398" fill="url(#drumGrad)" stroke="#fff" stroke-width="5"/>
</svg>

<h2 class="abs heading jobs-title">Job's Posting</h2>
<p class="abs jobs-intro">Meridel Haulage is an international carrier which provides service between Canada and the United States with domestic service in each country. Employment opportunities for both Canada and the United States are available. We are currently seeking Owner/Operators &amp; Company Drivers in the southern Ontario area.</p>
<table class="abs jobs-table">
  <tr>
    <td class="job-photo"><div role="img" aria-label="Photo of a truck driver in a safety vest"></div></td>
    <td class="job-text">Nam libero tempore, cum soluta nobis est eligendi optio ue nihil impedit quo minus id quod maxime placeat faceipossi mus, omnis voluptas assumenda est.</td>
    <td class="job-apply"><div class="btn-solid">APPLY NOW</div></td>
  </tr>
  <tr>
    <td class="job-photo"><div role="img" aria-label="Photo of a driver seated in a truck cab"></div></td>
    <td class="job-text">Nam libero tempore, cum soluta nobis est eligendi optio ue nihil impedit quo minus id quod maxime placeat faceipossi mus, omnis voluptas assumenda est.</td>
    <td class="job-apply"><div class="btn-solid">APPLY NOW</div></td>
  </tr>
  <tr>
    <td class="job-photo"><div role="img" aria-label="Photo of a driver leaning from a truck window"></div></td>
    <td class="job-text">Nam libero tempore, cum soluta nobis est eligendi optio ue nihil impedit quo minus id quod maxime placeat faceipossi mus, omnis voluptas assumenda est.</td>
    <td class="job-apply"><div class="btn-solid">APPLY NOW</div></td>
  </tr>
</table>
<div class="abs btn-outline view-btn">VIEW MORE</div>

<svg class="abs footer-bg" width="1200" height="621" viewBox="0 3090 1200 621">
  <polygon points="0,3192 891,3092 1200,3130 1200,3711 0,3711" fill="var(--footer)"/>
</svg>
<div class="abs footer-heading form-title">Contact Form</div>
<div class="abs field f1">First Name</div>
<div class="abs field f2">Last Name</div>
<div class="abs field f3">Email</div>
<div class="abs field f4">Phone Number</div>
<div class="abs field f5">Comments</div>
<div class="abs btn-solid submit">SUBMIT</div>

<div class="abs footer-heading info-title">Contact Information</div>
<div class="abs info-row" style="top:3329px">
  <span class="icon"><svg width="14" height="18" viewBox="0 0 14 18"><path d="M7 1a6 6 0 0 0-6 6c0 4.5 6 10 6 10s6-5.5 6-10a6 6 0 0 0-6-6z" fill="#fff"/><circle cx="7" cy="7" r="2.2" fill="#141414"/></svg></span>
  <span>480 Alder Ridge Rd.<br>Millbrook, ON K0L 2N0</span>
</div>
<div class="abs info-row" style="top:3404px">
  <span class="icon"><svg width="16" height="16" viewBox="0 0 16 16"><path d="M3.5 1.5l2.5 0 1.2 3.2-1.6 1.1a8 8 0 0 0 4.6 4.6l1.1-1.6 3.2 1.2 0 2.5c0 .8-.7 1.5-1.5 1.5A12 12 0 0 1 2 3c0-.8.7-1.5 1.5-1.5z" fill="#fff"/></svg></span>
  <span>1 800 555 0147</span>
</div>
<div class="abs info-row" style="top:3464px">
  <span class="icon"><svg width="16" height="12" viewBox="0 0 16 12"><rect x="0" y="0" width="16" height="12" rx="1.5" fill="#fff"/><polyline points="1,1 8,7 15,1" fill="none" stroke="#141414" stroke-width="1.5"/></svg></span>
  <span>info@meridelhaulage.com</span>
</div>
<div class="abs socials">
  <span style="background:#3b5998"></span>
  <span style="background:#a0663a"></span>
  <span style="background:#d6412f"></span>
  <span style="background:#c4221b"></span>
</div>
<div class="abs divider"></div>
<div class="abs copyright">Copyright © 2019, Meridel Haulage. All rights reserved.</div>

</body>
</html>
```